Criação de Papelaria Profissional para Consultoria de Negócios
" Somos uma empresa de consultoria para transportadoras, atuamos de forma operacional, fazemos um diagnóstico dos problemas da empresa, desenhamos processos, treinamos e auditamos o andamento, atuamos em todas os departamentos de uma transportadora. "

```html
<!DOCTYPE html>
<html lang="pt-BR">
<head>
<meta charset="UTF-8">
<title>Vetra Consultoria — Cartão de Visita</title>
<link rel="stylesheet" href="https://fonts.googleapis.com/css2?family=Montserrat:wght@400;500;600;800&display=swap">
<style>
  :root {
    --blue: #1f6fb8;
    --blue-light: #3a9ad9;
    --orange: #f07f1e;
    --ink: #3a3f47;
    --muted: #7a8089;
    --card: #ffffff;
    --card-shade: #f1f3f5;
    --backdrop: #2b2d31;
  }
  * { margin: 0; padding: 0; box-sizing: border-box; }
  html, body {
    width: 1200px; height: 1200px; overflow: hidden;
    background: var(--backdrop);
    font-family: "Montserrat", sans-serif;
  }
  .stationery {
    width: 1200px; height: 1200px;
    display: flex; flex-direction: column;
    align-items: center; justify-content: center; gap: 70px;
  }
  .card {
    position: relative;
    width: 900px; height: 500px;
    background: linear-gradient(135deg, var(--card) 55%, var(--card-shade));
    border-radius: 14px;
    overflow: hidden;
  }
  .card::after {
    content: ""; position: absolute; left: 0; right: 0; bottom: 0; height: 12px;
    background: linear-gradient(to bottom, var(--orange) 0 3px, var(--blue) 3px);
  }

  /* Front */
  .card-front .brand {
    position: absolute; left: 120px; top: 150px;
    display: flex; align-items: center; gap: 34px;
  }
  .brand-dot {
    width: 150px; height: 150px; border-radius: 50%;
    background: var(--blue);
  }
  .brand-name {
    color: var(--blue); font-weight: 800;
    font-size: 92px; line-height: 0.95; letter-spacing: 1px;
  }
  .brand-name span { display: block; font-size: 43px; letter-spacing: 6px; text-transform: uppercase; }

  /* Back */
  .card-back .accent-circle {
    position: absolute; left: -60px; top: -70px;
    width: 400px; height: 400px; border-radius: 50%;
    background: var(--blue-light);
  }
  .contact {
    position: absolute; left: 470px; top: 150px; color: var(--ink);
  }
  .contact-name { font-size: 34px; font-weight: 600; }
  .contact-role { font-size: 18px; color: var(--muted); margin: 4px 0 28px; }
  .contact-list { list-style: none; display: flex; flex-direction: column; gap: 10px; }
  .contact-list li { display: flex; align-items: center; gap: 14px; font-size: 15px; font-weight: 500; }
  .contact-list .company { font-weight: 600; }
  .icon {
    width: 26px; height: 26px; border-radius: 50%;
    background: var(--ink); flex: none;
    display: flex; align-items: center; justify-content: center;
  }
  .icon.plain-blue { background: var(--blue); }
  .icon.plain-orange { background: var(--orange); }
  .icon svg { width: 14px; height: 14px; }
</style>
</head>
<body>
<main class="stationery">

  <section class="card card-front">
    <div class="brand">
      <div class="brand-dot"></div>
      <div class="brand-name">Vetra<span>Consultoria</span></div>
    </div>
  </section>

  <section class="card card-back">
    <div class="accent-circle"></div>
    <div class="contact">
      <h1 class="contact-name">Nome Completo</h1>
      <p class="contact-role">Cargo</p>
      <ul class="contact-list">
        <li><span class="icon"><svg viewBox="0 0 24 24" fill="#fff"><path d="M6.6 10.8a15 15 0 0 0 6.6 6.6l2.2-2.2a1 1 0 0 1 1-.25 11.4 11.4 0 0 0 3.6.57 1 1 0 0 1 1 1V20a1 1 0 0 1-1 1A17 17 0 0 1 3 4a1 1 0 0 1 1-1h3.5a1 1 0 0 1 1 1c0 1.25.2 2.45.57 3.57a1 1 0 0 1-.25 1z"/></svg></span>(00) 0000-0000</li>
        <li><span class="icon"><svg viewBox="0 0 24 24" fill="#fff"><path d="M12 2a7 7 0 0 0-7 7c0 5 7 13 7 13s7-8 7-13a7 7 0 0 0-7-7zm0 9.5A2.5 2.5 0 1 1 12 6.5a2.5 2.5 0 0 1 0 5z"/></svg></span><span><span class="company">Vetra Consultoria</span><br>Rua das Palmeiras, 120 – Centro, São Paulo</span></li>
        <li><span class="icon"><svg viewBox="0 0 24 24" fill="none" stroke="#fff" stroke-width="2"><rect x="3" y="5" width="18" height="14" rx="2"/><path d="M3 7l9 6 9-6"/></svg></span>contato@vetraconsultoria.com.br</li>
        <li><span class="icon"><svg viewBox="0 0 24 24" fill="none" stroke="#fff" stroke-width="2"><circle cx="12" cy="12" r="9"/><path d="M3 12h18M12 3c3 3 3 15 0 18M12 3c-3 3-3 15 0 18"/></svg></span>www.vetraconsultoria.com.br</li>
        <li><span class="icon plain-blue"></span>/vetraconsultoria</li>
        <li><span class="icon plain-orange"></span>/vetraconsultoria</li>
      </ul>
    </div>
  </section>

</main>
</body>
</html>
```